High Tech Real Estate Startup needs a business card

We are developing an innovative real estate marketing product based around advanced search and virtual reality.

We talk to people, we need business cards.

Target Market(s)

The target market is technology professionals and realtors.

Contact Information for Business Card

The information to be included will include

Name
Title
Phone Number
E-mail Address
www.quelzo.com

It should use simple iconography for each one of those fields.

Font styles to use
Other font styles liked:
• Co, Jubilat, Avenir

Colors

Designer to choose colors to be used in the design.

Requirements
Must have
• Clean aesthetic,
• Good use of negative space.
• It should use our company logo, shown in the attached file. It is able to use the negative of that logo (coloured font and white background) and I have attached other acceptable accent colours in a swatch file.
Should not have
• Should not be too busy
• No extraneous text (slogans, tag lines etc)

```html
<!DOCTYPE html>
<html lang="en">
<head>
<meta charset="utf-8">
<title>Quelzo Business Card</title>
<link rel="stylesheet" href="https://fonts.googleapis.com/css2?family=Mulish:wght@400;500;600&display=swap">
<style>
  :root {
    --teal: #2cb8bd;
    --card-light: #e7e7e7;
    --ink-grey: #4a4a4a;
    --white: #ffffff;
    --backdrop: #f3f1ec;
  }
  * { margin: 0; padding: 0; box-sizing: border-box; }
  html, body {
    width: 1200px;
    height: 840px;
    overflow: hidden;
    background: var(--backdrop);
    font-family: "Mulish", "Avenir", sans-serif;
  }
  .canvas {
    position: relative;
    width: 1200px;
    height: 840px;
    display: flex;
    justify-content: center;
    align-items: center;
    gap: 80px;
  }
  .card {
    position: relative;
    width: 460px;
    height: 460px;
    box-shadow: 0 6px 18px rgba(0, 0, 0, 0.12);
  }
  .card--front {
    background: var(--card-light);
  }
  .logo-block {
    position: absolute;
    top: 30px;
    left: 50%;
    transform: translateX(-50%);
    width: 250px;
    height: 220px;
    background: var(--teal);
    display: flex;
    align-items: center;
    justify-content: center;
  }
  .wordmark {
    color: var(--white);
    font-weight: 500;
    letter-spacing: 0.06em;
  }
  .wordmark--small { font-size: 34px; }
  .details {
    position: absolute;
    top: 278px;
    left: 0;
    width: 100%;
    text-align: center;
  }
  .details__name {
    color: var(--teal);
    font-size: 26px;
    font-weight: 500;
    letter-spacing: 0.02em;
    text-transform: uppercase;
    line-height: 1.1;
  }
  .details__title {
    color: var(--ink-grey);
    font-size: 17px;
    margin-top: 2px;
  }
  .details__contact {
    list-style: none;
    margin-top: 22px;
    color: var(--ink-grey);
    font-size: 17px;
    line-height: 1.35;
  }
  .card--back {
    background: var(--teal);
    display: flex;
    align-items: center;
    justify-content: center;
  }
  .wordmark--large {
    font-size: 74px;
    letter-spacing: 0.05em;
  }
</style>
</head>
<body>
  <main class="canvas">
    <section class="card card--front" aria-label="Card front">
      <div class="logo-block">
        <span class="wordmark wordmark--small">QUELZO</span>
      </div>
      <div class="details">
        <p class="details__name">Jamie Korwin</p>
        <p class="details__title">General Manager</p>
        <ul class="details__contact">
          <li>616-555-0187</li>
          <li>info@quelzo.com</li>
          <li>www.quelzo.com</li>
        </ul>
      </div>
    </section>
    <section class="card card--back" aria-label="Card back">
      <span class="wordmark wordmark--large">QUELZO</span>
    </section>
  </main>
</body>
</html>
```